Out Door Living brochure

We need a Great looking brochure to feature the latest in out door living. Showcasing out doors is the new living space.

I'm enclosing our logo and a brochure we had done recently it didn't have enough impact. This one was a single fold you can also provide a tri fold if you see fit. We like the verbiage, but if you can spice it up we would love to see that. This brochure will be added to our sales packet.
Thank you!!!

Target Market(s)

Home owners

Industry/Entity Type

Construction Company

Logo Text

(See logo) Beautiful Homes Built to Last Introducing Outdoor living 2017

Font styles to use
Serif

Requirements
Must have
• Logo and
• Beautiful Homes Built to Last
• Introducing Outdoor living 2017
Nice to have
• Benefits of outdoor living
Should not have
• Bad photos if these don't work let me know we can get others to replace the sapce

```html
<!DOCTYPE html>
<html lang="en">
<head>
<meta charset="utf-8">
<title>Outdoor Living 2017 Brochure</title>
<link rel="stylesheet" href="https://fonts.googleapis.com/css2?family=Open+Sans:wght@400;600;700&display=swap">
<style>
  :root {
    --blue: #3a9fe3;
    --blue-light: #62b6ee;
    --blue-deep: #2b8ad0;
    --charcoal: #333333;
    --white: #ffffff;
    --ink-grey: #5e5e5e;
    --page-bg: #e9e9e9;
    --photo-pool-a: #4c5a66;
    --photo-pool-b: #9aa7ae;
    --photo-patio-a: #6e5440;
    --photo-patio-b: #d9c3a5;
  }
  html, body {
    margin: 0;
    padding: 0;
    width: 1200px;
    height: 848px;
    overflow: hidden;
    background: var(--page-bg);
    font-family: "Open Sans", Arial, sans-serif;
  }
  .spread {
    position: relative;
    width: 1200px;
    height: 848px;
    overflow: hidden;
  }
  .spread-art {
    position: absolute;
    inset: 0;
  }
  .tagline-top {
    position: absolute;
    left: 150px;
    top: 40px;
    width: 420px;
    margin: 0;
    text-align: right;
    color: var(--white);
    font-weight: 700;
    font-size: 25px;
    line-height: 1.25;
    text-shadow: 0 1px 3px rgba(0,0,0,.45);
  }
  .staycation {
    position: absolute;
    left: 130px;
    top: 345px;
    width: 440px;
    margin: 0;
    text-align: right;
    color: var(--ink-grey);
    font-weight: 400;
    font-size: 30px;
    line-height: 1.25;
    letter-spacing: .5px;
  }
  .back-brand {
    position: absolute;
    left: 60px;
    top: 650px;
    margin: 0;
    color: var(--white);
    font-size: 14px;
    font-weight: 600;
    letter-spacing: 2px;
  }
  .contact {
    position: absolute;
    left: 60px;
    top: 690px;
    margin: 0;
    color: var(--white);
    font-style: normal;
    font-size: 16px;
    line-height: 1.4;
  }
  .contact .phone { font-size: 19px; font-weight: 600; }
  .front-brand {
    position: absolute;
    left: 870px;
    top: 290px;
    width: 150px;
    text-align: center;
    margin: 0;
    color: var(--blue);
    font-size: 14px;
    font-weight: 600;
    line-height: 1.35;
    letter-spacing: 1px;
  }
  .cover-title {
    position: absolute;
    left: 660px;
    top: 450px;
    width: 500px;
    margin: 0;
    text-align: center;
    color: var(--white);
    font-weight: 400;
    font-size: 40px;
    line-height: 1.2;
    text-shadow: 0 1px 3px rgba(0,0,0,.2);
  }
  .cover-url {
    position: absolute;
    left: 720px;
    top: 566px;
    width: 400px;
    height: 38px;
    border-radius: 19px;
    background: var(--white);
    box-shadow: 0 3px 8px rgba(0,0,0,.25);
    color: var(--charcoal);
    font-size: 17px;
    line-height: 38px;
    text-align: center;
    letter-spacing: 1px;
  }
</style>
</head>
<body>
<main class="spread">
  <svg class="spread-art" width="1200" height="848" viewBox="0 0 1200 848" xmlns="http://www.w3.org/2000/svg">
    <defs>
      <linearGradient id="pool-photo" x1="0" y1="0" x2="1" y2="1">
        <stop offset="0" stop-color="var(--photo-pool-a)"/>
        <stop offset="1" stop-color="var(--photo-pool-b)"/>
      </linearGradient>
      <linearGradient id="patio-photo" x1="0" y1="0" x2="1" y2="1">
        <stop offset="0" stop-color="var(--photo-patio-a)"/>
        <stop offset="1" stop-color="var(--photo-patio-b)"/>
      </linearGradient>
      <linearGradient id="cover-blue" x1="0" y1="0" x2="0" y2="1">
        <stop offset="0" stop-color="var(--blue)"/>
        <stop offset="1" stop-color="var(--blue-light)"/>
      </linearGradient>
    </defs>

    <!-- back cover -->
    <rect class="back-panel" x="0" y="0" width="600" height="848" fill="var(--white)"/>
    <path class="photo-pool" role="img" aria-label="Photo of a modern backyard with a pool edge and a stone planter with a palm"
          d="M0,0 H600 V190 Q420,320 0,325 Z" fill="url(#pool-photo)"/>
    <path class="accent-line" d="M0,325 Q420,320 600,190" fill="none" stroke="var(--blue)" stroke-width="7"/>
    <path class="band-blue" d="M0,545 Q400,575 600,470 V848 H0 Z" fill="var(--blue)"/>
    <path class="band-dark" d="M0,570 Q400,598 585,500 Q470,660 440,848 H0 Z" fill="var(--charcoal)"/>

    <!-- front cover -->
    <rect class="front-panel" x="600" y="0" width="600" height="848" fill="url(#cover-blue)"/>
    <path class="photo-patio" role="img" aria-label="Photo of a covered patio lounge with wall lights, stone fireplace and outdoor sofas"
          d="M600,0 H1200 V280 Q900,360 800,450 Q700,470 600,470 Z" fill="url(#patio-photo)"/>
    <path class="front-wave" d="M600,470 Q700,470 800,450 Q900,360 1200,280 V300 Q920,380 820,470 Q720,500 600,500 Z" fill="var(--blue-deep)" opacity=".5"/>
    <circle class="brand-seal" cx="945" cy="320" r="78" fill="var(--white)" stroke="var(--blue)" stroke-width="6"/>
    <line class="fold" x1="600" y1="0" x2="600" y2="848" stroke="rgba(0,0,0,.12)" stroke-width="1"/>
  </svg>

  <p class="tagline-top">Innovative ideas that help stretch out the seasons, making it comfy and cozy.</p>
  <p class="staycation">Enjoy your staycation<br>in the comfort of your own<br>back yard</p>

  <p class="back-brand">HARBOR RIDGE BUILDERS</p>
  <address class="contact">
    <span class="phone">CALL: 555-014-2290</span><br>
    hello@harborridgemail.net<br>
    www.harborridgebuilders.com<br>
    1480 Marlow Lane, Bayview, CA 94000<br>
    HARBOR RIDGE
  </address>

  <p class="front-brand">HARBOR RIDGE BUILDERS</p>
  <h1 class="cover-title">Introducing<br>Outdoor living 2017</h1>
  <div class="cover-url">www.harborridgebuilders.com</div>
</main>
</body>
</html>
```